Letter Head Design

I need a letter head design based on my company logo that I attached.
Include phone number: (403)582-4316
Address: 347 14th Avenue NE, Calgary, Alberta, Canada, T3K 4R8

Industry/Entity Type

It Company

```html
<!DOCTYPE html>
<html lang="en">
<head>
<meta charset="utf-8">
<title>BrightRoom Interiors Corp. — Letterhead</title>
<link href="https://fonts.googleapis.com/css2?family=Open+Sans:wght@400;600;700&display=swap" rel="stylesheet">
<style>
  :root {
    --brand-green: #62d02c;
    --brand-blue: #2b55d8;
    --brand-blue-light: #3f8bf0;
    --mark-grey: #b9b9b9;
    --paper: #ffffff;
    --ink-white: #ffffff;
  }
  html, body {
    margin: 0;
    padding: 0;
    overflow: hidden;
    background: var(--paper);
  }
  .letterhead {
    position: relative;
    width: 927px;
    height: 1200px;
    overflow: hidden;
    background: var(--paper);
    font-family: "Open Sans", Arial, sans-serif;
  }

  /* Header brand block */
  .header-brand {
    position: absolute;
    top: 15px;
    left: 0;
    width: 927px;
    text-align: center;
  }
  .header-brand__square {
    display: block;
    width: 96px;
    height: 96px;
    margin: 0 auto;
    border-radius: 8px;
    background: var(--brand-blue);
  }
  .header-brand__name {
    display: block;
    margin-top: 8px;
    font-size: 31px;
    font-weight: 600;
    line-height: 1;
    color: var(--brand-blue);
    letter-spacing: -0.5px;
  }
  .header-brand__sub {
    display: block;
    margin-top: 2px;
    padding-left: 70px;
    font-size: 7px;
    font-weight: 600;
    letter-spacing: 1.5px;
    color: var(--brand-blue);
  }

  /* Contact bands */
  .contact-band {
    position: absolute;
    left: 0;
    width: 927px;
    height: 17px;
    line-height: 17px;
    text-align: center;
    font-size: 12px;
    font-weight: 400;
    color: var(--ink-white);
  }
  .contact-band--address { top: 164px; background: var(--brand-green); }
  .contact-band--phone   { top: 182px; background: var(--brand-blue); }

  /* Faint centre mark */
  .faint-mark {
    position: absolute;
    top: 577px;
    left: 205px;
    display: flex;
    align-items: center;
  }
  .faint-mark__square {
    width: 131px;
    height: 134px;
    border-radius: 8px;
    background: var(--mark-grey);
  }
  .faint-mark__text {
    margin-left: 28px;
    margin-top: 6px;
  }
  .faint-mark__name {
    display: block;
    font-size: 64px;
    font-weight: 600;
    line-height: 1;
    color: var(--mark-grey);
    letter-spacing: -1px;
  }
  .faint-mark__sub {
    display: block;
    text-align: right;
    margin-top: 2px;
    font-size: 14px;
    font-weight: 600;
    letter-spacing: 3px;
    color: var(--mark-grey);
  }

  /* Footer swoosh */
  .footer-swoosh {
    position: absolute;
    left: 0;
    top: 1080px;
    width: 927px;
    height: 120px;
  }
  .footer-brand {
    position: absolute;
    top: 1124px;
    left: 700px;
    display: flex;
    align-items: center;
  }
  .footer-brand__square {
    width: 48px;
    height: 52px;
    border-radius: 4px;
    background: var(--ink-white);
  }
  .footer-brand__text { margin-left: 10px; }
  .footer-brand__name {
    display: block;
    font-size: 22px;
    font-weight: 600;
    line-height: 1;
    color: var(--ink-white);
  }
  .footer-brand__sub {
    display: block;
    text-align: right;
    font-size: 5px;
    font-weight: 600;
    letter-spacing: 1px;
    color: var(--ink-white);
  }
</style>
</head>
<body>
<main class="letterhead">

  <header class="header-brand">
    <span class="header-brand__square"></span>
    <span class="header-brand__name">BrightRoom</span>
    <span class="header-brand__sub">Interiors Corp.</span>
  </header>

  <div class="contact-band contact-band--address">Address: 347 14th Avenue NE, Calgary, Alberta, Canada, T3K 4R8</div>
  <div class="contact-band contact-band--phone">phone number: (403)582-4316</div>

  <div class="faint-mark" aria-hidden="true">
    <span class="faint-mark__square"></span>
    <span class="faint-mark__text">
      <span class="faint-mark__name">BrightRoom</span>
      <span class="faint-mark__sub">Interiors Corp.</span>
    </span>
  </div>

  <svg class="footer-swoosh" viewBox="0 1080 927 120" aria-hidden="true">
    <defs>
      <linearGradient id="swoosh-blue" x1="0" y1="0" x2="0" y2="1">
        <stop offset="0" stop-color="var(--brand-blue-light)"/>
        <stop offset="1" stop-color="var(--brand-blue)"/>
      </linearGradient>
    </defs>
    <polygon points="685,1088 927,1088 927,1200 580,1200 580,1193 600,1193" fill="var(--brand-green)"/>
    <rect x="0" y="1186" width="927" height="6" fill="var(--brand-green)"/>
    <polygon points="695,1096 927,1096 927,1200 612,1200" fill="url(#swoosh-blue)"/>
  </svg>

  <div class="footer-brand">
    <span class="footer-brand__square"></span>
    <span class="footer-brand__text">
      <span class="footer-brand__name">BrightRoom</span>
      <span class="footer-brand__sub">Interiors Corp.</span>
    </span>
  </div>

</main>
</body>
</html>
```